Business Card Design Project

Basketball Training program

Offers: Travel Club Program - Camps - Clinics - Private Training

website: ridgeportcourt.net
Phone Contact: Main Phone: 555-314-7720
Email: ridgeport.court@mailzone.example

Industry/Entity Type

Business

Contact Information for Business Card

Need one for the following coaches:
Marcus Thorne - Boys & Girls Basketball Coach
Kirasol Vendry - Girls Basketball Coach
Anselmo Trujar - Director/Head Coach
Walter Fisk- Boys Basketball
Howard Lindqvist - Boys Basketball
Ramon Etxeberri - Boys Basketball
Talvin Okafor- Boys Basketball/ Trainer
Al Hargrove - Boys & Girls Basketball Coach

Basketball Training program Logo - one side

Logo on the corner
new one on the left (RC)
old one on the right (old one is with the ridgeport and court)

```html
<!DOCTYPE html>
<html lang="en">
<head>
<meta charset="utf-8">
<title>Marcus Thorne – Ridgeport Court Business Card</title>
<link rel="stylesheet" href="https://fonts.googleapis.com/css2?family=Domine:wght@700&display=swap">
<style>
  :root {
    --card-black: #141414;
    --card-charcoal: #232323;
    --gold: #f7ae0c;
    --pale-gold: #fbdc8a;
    --ink: #0b0b0b;
    --glow: rgba(250, 235, 170, 0.55);
  }
  html, body {
    margin: 0;
    padding: 0;
    width: 1200px;
    height: 720px;
    overflow: hidden;
    background: var(--card-black);
  }
  .card {
    position: relative;
    width: 1200px;
    height: 720px;
    overflow: hidden;
    background: radial-gradient(ellipse at 50% 40%, var(--card-charcoal) 0%, var(--card-black) 70%);
    font-family: "Domine", Georgia, serif;
    font-weight: 700;
  }
  .backdrop-art {
    position: absolute;
    left: 420px;
    top: 110px;
    width: 360px;
    height: 300px;
    border-radius: 50%;
    background: radial-gradient(circle, rgba(60, 60, 60, 0.35) 0%, rgba(20, 20, 20, 0) 70%);
  }
  .monogram {
    position: absolute;
    left: 109px;
    top: 96px;
    width: 182px;
    height: 182px;
    border-radius: 50%;
    border: 10px solid var(--ink);
    box-sizing: border-box;
    background: var(--card-black);
    box-shadow: 0 0 14px 4px var(--glow);
    display: flex;
    align-items: center;
    justify-content: center;
    color: var(--gold);
    font-size: 64px;
    letter-spacing: 2px;
  }
  .brand {
    position: absolute;
    right: 70px;
    top: 160px;
    display: flex;
    align-items: center;
    gap: 14px;
    color: var(--gold);
    font-size: 34px;
  }
  .brand-dot {
    width: 38px;
    height: 38px;
    border-radius: 50%;
    background: var(--gold);
  }
  .identity {
    position: absolute;
    left: 0;
    right: 0;
    top: 268px;
    text-align: center;
    color: var(--gold);
    text-shadow: 0 0 4px var(--ink), 0 2px 3px var(--ink), 0 0 10px rgba(0,0,0,0.9);
  }
  .coach-name {
    margin: 0;
    font-size: 74px;
    line-height: 1;
    font-weight: 700;
  }
  .coach-role {
    margin: 12px 0 0;
    font-size: 43px;
    line-height: 1;
    font-weight: 700;
  }
  .contacts {
    position: absolute;
    left: 226px;
    top: 428px;
    margin: 0;
    padding: 0;
    list-style: none;
  }
  .contact {
    display: flex;
    align-items: center;
    height: 70px;
    color: var(--pale-gold);
    font-size: 34px;
    text-shadow: 0 0 3px var(--ink), 0 2px 3px var(--ink);
  }
  .contact-icon {
    width: 62px;
    height: 62px;
    margin-right: 36px;
    flex: none;
  }
</style>
</head>
<body>
<main class="card">
  <div class="backdrop-art" role="img" aria-label="Faint basketball and hoop background decoration"></div>

  <div class="monogram">RC</div>

  <div class="brand">
    <span class="brand-dot"></span>
    <span class="brand-name">Ridgeport Court</span>
  </div>

  <header class="identity">
    <h1 class="coach-name">Marcus Thorne</h1>
    <p class="coach-role">Boys &amp; Girls Basketball Coach</p>
  </header>

  <ul class="contacts">
    <li class="contact">
      <svg class="contact-icon" viewBox="0 0 62 62" aria-hidden="true">
        <circle cx="31" cy="31" r="27" fill="#f7ae0c" stroke="#0b0b0b" stroke-width="3"/>
        <ellipse cx="31" cy="31" rx="12" ry="27" fill="none" stroke="#0b0b0b" stroke-width="2.5"/>
        <line x1="31" y1="4" x2="31" y2="58" stroke="#0b0b0b" stroke-width="2.5"/>
        <rect x="4" y="24" width="54" height="14" fill="#0b0b0b"/>
        <text x="31" y="35" text-anchor="middle" font-family="Arial, sans-serif" font-size="11" font-weight="700" fill="#f7ae0c">www</text>
      </svg>
      <span>Website: ridgeportcourt.net</span>
    </li>
    <li class="contact">
      <svg class="contact-icon" viewBox="0 0 62 62" aria-hidden="true">
        <path d="M14 8 L24 8 L28 20 L21 26 C25 35 30 40 38 44 L44 37 L56 41 L56 51 C56 55 52 58 48 57 C28 54 10 36 7 16 C6 12 10 8 14 8 Z" fill="#f7ae0c" stroke="#0b0b0b" stroke-width="3" stroke-linejoin="round"/>
      </svg>
      <span>Main Phone: 555-314-7720</span>
    </li>
    <li class="contact">
      <svg class="contact-icon" viewBox="0 0 62 62" aria-hidden="true">
        <rect x="6" y="14" width="50" height="36" rx="3" fill="#f7ae0c" stroke="#0b0b0b" stroke-width="3"/>
        <polyline points="8,17 31,36 54,17" fill="none" stroke="#0b0b0b" stroke-width="3" stroke-linejoin="round"/>
        <line x1="8" y1="48" x2="25" y2="31" stroke="#0b0b0b" stroke-width="3"/>
        <line x1="54" y1="48" x2="37" y2="31" stroke="#0b0b0b" stroke-width="3"/>
      </svg>
      <span>Email: ridgeport.court@mailzone.example</span>
    </li>
  </ul>
</main>
</body>
</html>
```